Business card with professional look

I would like a creative yet professional looking business card for our business. We sell broadcast TV related security products for mobile phones, set top boxes, and tablets. Our customers are international. We have a logo we like and I would like to possibly add some color to the business card but keep it professional looking.

Target Market(s)

Professionals in the TV, cable, ans Satellite industries

Industry/Entity Type

Cable Tv

Contact Information for Business Card

Name Ned Vastermill, title CEO, Address 8130 Harborline Court, Suite 400, Del Arvo, CA 91584 USA, phone numbers m:+1.619.284.7302 o:+1.855.672.9140, email, logo

Font styles to use
Other font styles liked:
• Open to any font that looks good with logo

Requirements
Must have
• professional look with colors coordinated with logo colors. would like to add one or two different colors as well as some form of background color

```html
<!DOCTYPE html>
<html lang="en">
<head>
<meta charset="utf-8">
<title>Vantlocast Business Card</title>
<link rel="stylesheet" href="https://fonts.googleapis.com/css2?family=Roboto:wght@400;500;700&display=swap">
<style>
  :root {
    --backdrop: #3b3b3b;
    --card-white: #ffffff;
    --brand-blue: #1565b8;
    --brand-blue-light: #1f88cf;
    --brand-blue-deep: #17479a;
    --ink-dark: #2b2b2b;
    --ink-grey: #3d3d3d;
    --on-blue: #ffffff;
    --mark-faint: #263f8c;
  }
  * { box-sizing: border-box; margin: 0; padding: 0; }
  html, body {
    width: 1200px; height: 1200px; overflow: hidden;
    background: var(--backdrop);
    font-family: "Roboto", Arial, sans-serif;
  }
  .card {
    position: absolute; left: 240px; width: 720px; height: 409px;
    border-radius: 19px; overflow: hidden;
  }
  .card-front {
    top: 162px;
    background: radial-gradient(ellipse 60% 70% at 62% 68%, #d4d6db 0%, #f4f4f6 55%, var(--card-white) 80%);
  }
  .card-back {
    top: 630px;
    background: radial-gradient(ellipse 55% 60% at 50% 55%, var(--brand-blue-light) 0%, var(--brand-blue) 55%, var(--brand-blue-deep) 100%);
  }
  .contact-panel { position: absolute; left: 0; top: 0; width: 720px; height: 409px; }
  .person { position: absolute; left: 33px; top: 86px; }
  .person-name { font-size: 29px; font-weight: 700; color: var(--brand-blue); line-height: 1.1; }
  .person-title { font-size: 19px; color: var(--ink-dark); line-height: 1.2; }
  .brand-lockup {
    position: absolute; display: flex; align-items: center; gap: 12px;
  }
  .card-front .brand-lockup { right: 52px; top: 86px; }
  .brand-name { font-weight: 700; letter-spacing: -1px; }
  .card-front .brand-name { font-size: 52px; color: var(--ink-grey); }
  .brand-square { width: 18px; height: 18px; background: var(--brand-blue); }
  .card-back .brand-lockup { left: 0; right: 0; top: 160px; justify-content: center; }
  .card-back .brand-name { font-size: 72px; color: var(--mark-faint); }
  .card-back .brand-square { width: 24px; height: 24px; background: var(--mark-faint); }
  .address {
    position: absolute; left: 33px; top: 213px;
    font-size: 19px; line-height: 24px; color: var(--on-blue);
  }
  .contact-list { position: absolute; left: 30px; top: 279px; list-style: none; }
  .contact-list li {
    display: flex; align-items: center; gap: 9px;
    height: 24px; font-size: 19px; color: var(--on-blue);
  }
  .contact-list svg { width: 17px; height: 17px; flex: none; }
  .site-url {
    position: absolute; left: 0; right: 0; top: 366px;
    text-align: center; font-size: 19px; color: var(--on-blue);
  }
</style>
</head>
<body>
  <section class="card card-front">
    <svg class="contact-panel" viewBox="0 0 720 409" aria-hidden="true">
      <defs>
        <radialGradient id="panelGlow" cx="0.55" cy="0.6" r="0.7">
          <stop offset="0" stop-color="#1e84cc"/>
          <stop offset="1" stop-color="#1656a8"/>
        </radialGradient>
      </defs>
      <path d="M0 198 L388 171 Q414 169 418 196 L434 409 L0 409 Z" fill="url(#panelGlow)"/>
    </svg>

    <div class="person">
      <p class="person-name">Ned Vastermill</p>
      <p class="person-title">CEO</p>
    </div>

    <div class="brand-lockup">
      <span class="brand-name">Vantlocast</span>
      <span class="brand-square"></span>
    </div>

    <p class="address">8130 Harborline Court, Suite 400<br>Del Arvo, CA 91584 USA</p>

    <ul class="contact-list">
      <li>
        <svg viewBox="0 0 16 16"><rect x="3.5" y="1" width="9" height="14" rx="1.5" fill="none" stroke="#fff" stroke-width="1.4"/><circle cx="8" cy="12.6" r="0.9" fill="#fff"/></svg>
        m:+1.619.284.7302
      </li>
      <li>
        <svg viewBox="0 0 16 16"><path d="M1 6 Q8 1 15 6 L13.5 8 L11 7 L11 5.5 Q8 4.5 5 5.5 L5 7 L2.5 8 Z" fill="#fff"/><path d="M3 9 L13 9 L14 14 L2 14 Z" fill="#fff"/><circle cx="8" cy="11.3" r="1.6" fill="#1a6cbd"/></svg>
        o:+1.855.672.9140
      </li>
      <li>
        <svg viewBox="0 0 16 16"><rect x="1" y="3" width="14" height="10" fill="none" stroke="#fff" stroke-width="1.4"/><path d="M1 3 L8 9 L15 3 M1 13 L6 7.5 M15 13 L10 7.5" fill="none" stroke="#fff" stroke-width="1.4"/></svg>
        nedv@vantlocast.net
      </li>
      <li>
        <svg viewBox="0 0 16 16" fill="none" stroke="#fff" stroke-width="1.1"><circle cx="8" cy="8" r="6.8"/><ellipse cx="8" cy="8" rx="3" ry="6.8"/><path d="M1.2 8 H14.8 M2.3 4.5 H13.7 M2.3 11.5 H13.7"/></svg>
        www.vantlocast.net
      </li>
    </ul>
  </section>

  <section class="card card-back">
    <div class="brand-lockup">
      <span class="brand-name">Vantlocast</span>
      <span class="brand-square"></span>
    </div>
    <p class="site-url">www.vantlocast.net</p>
  </section>
</body>
</html>
```